Sports / Entertainment Media Co needs a biz card design

We are a media co / luxury lifestyle brand that targets professional athletes, entertainers and high net-worth fans. We are currently preparing for a relaunch and in need for new biz cards. I envision a black on black card with a pop of color on opposite side. Color Palette black, white, red etc. I want this card to exude sexiness and power. Very high stylized, hip and cool. I have attached the logo - I would like to see it all in black, but also open to other ideas. I will also upload a current card with all information needed on this new card. Furthermore I will add some samples of other cards I love. Thanks!!!

I provided suggestions, however I am open to all ideas!!   Be as creative as you can.  Think cutting-edge, sexy and powerful.  Take a look at the cards I uploaded to get a sense for what I like.  Thanks!!!

Entertainment

```html
<!DOCTYPE html>
<html lang="en">
<head>
<meta charset="utf-8">
<title>Pulse Media Ventures – Business Card</title>
<link rel="stylesheet" href="https://fonts.googleapis.com/css2?family=Poppins:wght@300;400;500&display=swap">
<style>
  :root {
    --backdrop: #2b2b2b;
    --card: #262626;
    --card-edge: #303030;
    --brand-dark: #151515;
    --accent: #e0222a;
    --text-light: #d9d9d9;
    --text-muted: #8a8a8a;
  }
  * { margin: 0; padding: 0; box-sizing: border-box; }
  html, body { width: 1200px; height: 1041px; overflow: hidden; background: var(--backdrop); }
  .canvas {
    width: 1200px; height: 1041px;
    display: flex; justify-content: center; align-items: center; gap: 90px;
    font-family: "Poppins", sans-serif;
  }
  .card {
    position: relative; width: 440px; height: 780px;
    background: var(--card); border-radius: 38px; overflow: hidden;
    box-shadow: 0 0 0 1px var(--card-edge), 0 24px 50px rgba(0,0,0,.45);
  }
  /* front */
  .front-brand {
    position: absolute; left: 44px; bottom: 96px;
    font-weight: 500; font-size: 72px; line-height: 1;
    color: var(--brand-dark);
  }
  .front-web {
    position: absolute; left: 46px; bottom: 50px;
    font-weight: 500; font-size: 24px; line-height: 1;
    color: var(--text-muted);
  }
  /* back */
  .identity { position: absolute; left: 60px; top: 70px; }
  .name { font-weight: 400; font-size: 26px; letter-spacing: 1px; text-transform: uppercase; color: var(--text-muted); }
  .name .first { color: var(--accent); }
  .role { margin-top: 4px; font-weight: 300; font-size: 14px; letter-spacing: 1px; text-transform: uppercase; color: var(--text-light); }
  .contacts { position: absolute; left: 92px; top: 220px; width: 320px; font-weight: 300; font-size: 14px; color: var(--text-light); }
  .contact-row { display: flex; gap: 28px; margin-bottom: 26px; }
  .contact { display: flex; align-items: flex-start; gap: 10px; }
  .contact svg { width: 15px; height: 15px; flex: none; margin-top: 2px; fill: var(--accent); }
  .accent-dot {
    position: absolute; right: 60px; bottom: 190px;
    width: 120px; height: 120px; border-radius: 50%;
    background: var(--accent);
  }
</style>
</head>
<body>
<main class="canvas">
  <section class="card card-front" aria-label="Card front">
    <div class="front-brand">Pulse</div>
    <div class="front-web">pulsemagazine.com</div>
  </section>

  <section class="card card-back" aria-label="Card back">
    <div class="identity">
      <p class="name"><span class="first">Dara</span> Kessler</p>
      <p class="role">Pres | Pulse Media Ventures LLC</p>
    </div>
    <div class="contacts">
      <div class="contact-row">
        <div class="contact">
          <svg viewBox="0 0 16 16" aria-hidden="true"><path d="M8 0a5.5 5.5 0 0 0-5.5 5.5C2.5 9.6 8 16 8 16s5.5-6.4 5.5-10.5A5.5 5.5 0 0 0 8 0zm0 8a2.5 2.5 0 1 1 0-5 2.5 2.5 0 0 1 0 5z"/></svg>
          <span>2240 NE 31st Avenue,<br>Ste 500, Miami, FL 33181</span>
        </div>
      </div>
      <div class="contact-row">
        <div class="contact">
          <svg viewBox="0 0 16 16" aria-hidden="true"><path d="M3.6 1l2.6 3.2-1.5 1.9a10 10 0 0 0 5.2 5.2l1.9-1.5L15 12.4 13.4 15C6.8 14.6 1.4 9.2 1 2.6z"/></svg>
          <span>305.555.0142</span>
        </div>
        <div class="contact">
          <svg viewBox="0 0 16 16" aria-hidden="true"><path d="M4 0h8a1 1 0 0 1 1 1v14a1 1 0 0 1-1 1H4a1 1 0 0 1-1-1V1a1 1 0 0 1 1-1zm1 2v10h6V2zm3 11a1 1 0 1 0 0 2 1 1 0 0 0 0-2z"/></svg>
          <span>954.555.0187</span>
        </div>
      </div>
      <div class="contact-row">
        <div class="contact">
          <svg viewBox="0 0 16 16" aria-hidden="true"><path d="M4 1h7v4H4zM1 6h14v7h-3v2H4v-2H1zm4 4v4h6v-4z"/></svg>
          <span>305.555.0193</span>
        </div>
      </div>
      <div class="contact-row">
        <div class="contact">
          <svg viewBox="0 0 16 16" aria-hidden="true"><path d="M0 3h16v10H0zm1.5 1.2L8 9l6.5-4.8V4h-13z"/></svg>
          <span>dara@pulsemagazine.com</span>
        </div>
      </div>
    </div>
    <div class="accent-dot" aria-hidden="true"></div>
  </section>
</main>
</body>
</html>
```